Outdoor mass notification company needing business card design.

Our company name is Harborline Signal Systems Inc located in Amory Mississippi and we sell and maintain "Corvath" Mass Notification Sirens in the US. Outdoor sirens notify people of certain severe dangers such as tornados, severe thunderstorms, flooding, hurricanes and tsunamis. We also serve the oil and gas refining industries to warn of Chemical releases, fires, and lightning alerts.

Contact Information for Business Card

Name, title, cell number, email address

Requirements
Nice to have
• The Corvath logo and also the Tallbrook logo.

```html
<!DOCTYPE html>
<html lang="en">
<head>
<meta charset="utf-8">
<title>Harborline Signal Systems – Business Card</title>
<link href="https://fonts.googleapis.com/css2?family=Roboto+Slab:wght@400;700&display=swap" rel="stylesheet">
<style>
  :root {
    --backdrop: #d3d4d6;
    --navy: #2c4a6a;
    --navy-deep: #2f4d6a;
    --navy-light: #3d6181;
    --paper: #ffffff;
    --ink-grey: #555a5e;
    --siren-dark: #1f1f1f;
    --siren-mid: #4a4a4a;
  }
  * { margin: 0; padding: 0; box-sizing: border-box; }
  html, body {
    width: 900px; height: 1200px; overflow: hidden;
    background: var(--backdrop);
    font-family: "Roboto Slab", serif;
  }
  .card {
    position: absolute; left: 133px; width: 633px; height: 364px;
  }
  .card--front {
    top: 210px;
    background: linear-gradient(100deg, var(--navy-deep), var(--navy-light));
    display: flex; align-items: center; justify-content: center;
  }
  .card--back { top: 624px; background: var(--paper); }

  .wordmark { font-weight: 700; line-height: 1.05; text-align: right; }
  .wordmark span { display: block; }
  .card--front .wordmark { color: var(--paper); }
  .card--front .wordmark .line-1 { font-size: 46px; }
  .card--front .wordmark .line-2 { font-size: 35px; }

  .card--back .wordmark {
    position: absolute; right: 354px; top: 160px; color: var(--navy);
  }
  .card--back .wordmark .line-1 { font-size: 27px; }
  .card--back .wordmark .line-2 { font-size: 21px; }

  .siren-photo {
    position: absolute; left: 298px; top: 122px; width: 37px; height: 124px;
    background: linear-gradient(180deg, var(--siren-dark) 0%, var(--siren-mid) 65%, var(--siren-dark) 100%);
  }

  .contact { position: absolute; left: 354px; top: 118px; }
  .contact__name { font-size: 24px; font-weight: 700; color: var(--navy); letter-spacing: 0.3px; }
  .contact__title { font-size: 16px; color: var(--ink-grey); margin-top: 2px; }
  .contact__list { list-style: none; margin-top: 14px; }
  .contact__list li {
    display: flex; align-items: center; gap: 8px;
    font-size: 14px; color: var(--ink-grey); letter-spacing: 1px;
    height: 22.5px;
  }
  .contact__list svg { width: 14px; height: 14px; fill: var(--navy); flex: none; }

  .address {
    position: absolute; left: 0; right: 0; top: 280px; text-align: center;
    color: var(--ink-grey); font-size: 16.5px; letter-spacing: 0.3px;
  }
  .address svg { display: block; margin: 0 auto 8px; width: 12px; height: 16px; fill: var(--navy); }
</style>
</head>
<body>
  <section class="card card--front">
    <div class="wordmark">
      <span class="line-1">HARBORLINE</span>
      <span class="line-2">SIGNAL SYSTEMS</span>
    </div>
  </section>

  <section class="card card--back">
    <div class="wordmark">
      <span class="line-1">HARBORLINE</span>
      <span class="line-2">SIGNAL SYSTEMS</span>
    </div>

    <div class="siren-photo" role="img" aria-label="Photo of an outdoor mass notification siren on a pole"></div>

    <div class="contact">
      <div class="contact__name">DANA WHITFIELD</div>
      <div class="contact__title">Owner</div>
      <ul class="contact__list">
        <li>
          <svg viewBox="0 0 24 24"><path d="M6.6 10.8a15.1 15.1 0 0 0 6.6 6.6l2.2-2.2a1 1 0 0 1 1-.25 11.4 11.4 0 0 0 3.6.57 1 1 0 0 1 1 1V20a1 1 0 0 1-1 1A17 17 0 0 1 3 4a1 1 0 0 1 1-1h3.5a1 1 0 0 1 1 1c0 1.25.2 2.45.57 3.57a1 1 0 0 1-.25 1z"/></svg>
          (662) 555-0147
        </li>
        <li>
          <svg viewBox="0 0 24 24"><path d="M2 5h20v14H2z M3.5 6.5 12 13l8.5-6.5" fill="var(--navy)"/><path d="M3 6l9 7 9-7" fill="none" stroke="#fff" stroke-width="1.6"/></svg>
          info@harborlinesignal.com
        </li>
        <li>
          <svg viewBox="0 0 24 24"><circle cx="12" cy="12" r="10" fill="none" stroke="var(--navy)" stroke-width="2"/><path d="M2 12h20M12 2v20M12 2c-4 5-4 15 0 20M12 2c4 5 4 15 0 20" fill="none" stroke="var(--navy)" stroke-width="1.5"/></svg>
          www.harborlinesignal.com
        </li>
      </ul>
    </div>

    <div class="address">
      <svg viewBox="0 0 12 16"><path d="M6 0a6 6 0 0 0-6 6c0 4.5 6 10 6 10s6-5.5 6-10a6 6 0 0 0-6-6zm0 8.2A2.2 2.2 0 1 1 6 3.8a2.2 2.2 0 0 1 0 4.4z"/></svg>
      1480 Riverbend Rd Amory, MS 38821
    </div>
  </section>
</body>
</html>
```